Vesperine: A Biblical Short Story Collection

I'm looking for a book cover for a biblical short story retelling: black background, with the image of a wine goblet (ancient looking if at all possible) filled with water, with a trace of red wine indicating that it is changing. The title is Vesperine and the subtitle is A Biblical Short Story Collection. The author name is Nora Fenwick.

```html
<!DOCTYPE html>
<html lang="en">
<head>
<meta charset="utf-8">
<title>Vesperine — Book Cover</title>
<link rel="stylesheet" href="https://fonts.googleapis.com/css2?family=Cinzel:wght@400;500&family=Marcellus&display=swap">
<style>
  :root {
    --stage: #e4e2de;
    --cover-black: #0d0d0e;
    --cover-edge: #1b1b1d;
    --title-red: #c8232b;
    --ink-white: #eeeeec;
    --glass-light: #9ea3a6;
    --glass-dark: #1c1d1f;
    --wine-red: #a3121b;
  }
  * { margin: 0; padding: 0; box-sizing: border-box; }
  html, body {
    width: 1200px;
    height: 789px;
    overflow: hidden;
    background: var(--stage);
  }
  .canvas {
    width: 1200px;
    height: 789px;
    display: flex;
    align-items: center;
    justify-content: center;
  }
  .book-cover {
    position: relative;
    width: 540px;
    height: 715px;
    background: radial-gradient(ellipse at 50% 45%, var(--cover-edge) 0%, var(--cover-black) 70%);
    color: var(--ink-white);
    text-align: center;
  }
  .title {
    position: absolute;
    top: 74px;
    left: 0;
    right: 0;
    font-family: "Cinzel", serif;
    font-weight: 400;
    font-size: 76px;
    letter-spacing: 3px;
    color: var(--title-red);
    line-height: 1;
  }
  .subtitle {
    position: absolute;
    top: 178px;
    left: 0;
    right: 0;
    font-family: "Marcellus", serif;
    font-size: 17px;
    letter-spacing: 3.5px;
    text-transform: uppercase;
    color: var(--ink-white);
  }
  .goblet-art {
    position: absolute;
    top: 258px;
    left: 50%;
    width: 170px;
    height: 310px;
    transform: translateX(-50%);
  }
  .author {
    position: absolute;
    bottom: 56px;
    left: 0;
    right: 0;
    font-family: "Cinzel", serif;
    font-weight: 400;
    font-size: 30px;
    letter-spacing: 11px;
    text-transform: uppercase;
    color: var(--ink-white);
  }
</style>
</head>
<body>
  <main class="canvas">
    <article class="book-cover">
      <h1 class="title">Vesperine</h1>
      <p class="subtitle">A Biblical Short Story Collection</p>
      <svg class="goblet-art" viewBox="0 0 170 310" role="img" aria-label="Photograph of a crystal wine goblet filled with water, a swirl of red wine spreading through it">
        <defs>
          <radialGradient id="goblet-tone" cx="50%" cy="30%" r="65%">
            <stop offset="0%" stop-color="var(--wine-red)" stop-opacity="0.55"/>
            <stop offset="35%" stop-color="var(--glass-light)" stop-opacity="0.55"/>
            <stop offset="100%" stop-color="var(--glass-dark)" stop-opacity="0.9"/>
          </radialGradient>
        </defs>
        <rect x="0" y="0" width="170" height="310" rx="12" fill="url(#goblet-tone)"/>
      </svg>
      <p class="author">Nora Fenwick</p>
    </article>
  </main>
</body>
</html>
```